Poster of Insipirational Quotes

Attached is a list of leadership quotes from Arlen Drubeck. I would like a poster made, incorporating whatever design elements you like, potentially including Arlen's face, and one or more of the quotes. I intend to print this out in A3 or larger to hang on my wall.

The quotes are:

Being responsible sometimes means pissing people off.

The day soldiers stop bringing you their problems is the day you have stopped leading them.

Don't be buffaloed by experts and elites. Experts often possess more data than judgment. Elites can become so inbred that they produce hemophiliacs who bleed to death as soon as they are nicked by the real world.

Don't be afraid to challenge the pros, even in their own backyard.

Never neglect details. When everyone's mind is dulled or distracted the leader must be doubly vigilant.

You don't know what you can get away with until you try.

Keep looking below surface appearances. Don't shrink from doing so (just) because you might not like what you find.

Organization doesn't really accomplish anything. Plans don't accomplish anything, either. Theories of management don't much matter. Endeavors succeed or fail because of the people involved. Only by attracting the best people will you accomplish great deeds.

Organization charts and fancy titles count for next to nothing.

Never let your ego get so close to your position that when your position goes, your ego goes with it.

Fit no stereotypes. Don't chase the latest management fads. The situation dictates which approach best accomplishes the team's mission.

Perpetual optimism is a force multiplier.

Look for intelligence and judgment, and most critically, a capacity to anticipate, to see around corners. Also look for loyalty, integrity, a high energy drive, a balanced ego, and the drive to get things done.

Great leaders are almost always great simplifiers, who can cut through argument, debate and doubt, to offer a solution everybody can understand.

The commander in the field is always right and the rear echelon is wrong, unless proved otherwise.

Have fun in your command. Don't always run at a breakneck pace. Take leave when you've earned it: Spend time with your families. Corollary: surround yourself with people who take their work seriously, but not themselves, those who work hard and play hard.

Command is lonely.

Leadership is the art of accomplishing more than the science of management
says is possible.
Updates

I need to modify the specification based on the designs that I've seen.

Target Market(s)

Executive Office

Colors

Designer to choose colors to be used in the design.

Requirements
Must have
• Quotes

```html
<!DOCTYPE html>
<html lang="en">
<head>
<meta charset="utf-8">
<title>Leadership Quotes Poster</title>
<link rel="stylesheet" href="https://fonts.googleapis.com/css2?family=Roboto:wght@400&family=Archivo+Black&display=swap">
<style>
  :root {
    --frame: #c4c4c4;
    --paper: #ffffff;
    --ink: #1c1c1c;
    --mark: #bdbdbd;
    --portrait-light: #e2e2e2;
    --portrait-dark: #d2d2d2;
  }
  html, body {
    margin: 0;
    padding: 0;
    width: 848px;
    height: 1200px;
    overflow: hidden;
    background: var(--frame);
  }
  .poster {
    position: relative;
    width: 848px;
    height: 1200px;
    background: var(--frame);
  }
  .sheet {
    position: absolute;
    left: 22px;
    top: 22px;
    width: 798px;
    height: 1148px;
    background: var(--paper);
    overflow: hidden;
  }
  .portrait-area {
    position: absolute;
    left: 53px;
    top: 150px;
    width: 708px;
    height: 775px;
    z-index: 0;
  }
  .quote-mark {
    position: absolute;
    z-index: 1;
    font-family: "Archivo Black", "Arial Black", sans-serif;
    color: var(--mark);
    font-size: 194px;
    line-height: 1;
    margin: 0;
  }
  .quote-mark--open { left: 66px; top: 52px; }
  .quote-mark--close { left: 648px; top: 1010px; }
  .quotes {
    position: absolute;
    z-index: 2;
    left: 72px;
    top: 117px;
    width: 700px;
    margin: 0;
    padding: 0;
    list-style: none;
    font-family: "Roboto", Arial, sans-serif;
    font-size: 16px;
    line-height: 19.5px;
    color: var(--ink);
  }
  .quotes li { margin: 0 0 18.7px; }
  .lead-letter { font-size: 21px; }
</style>
</head>
<body>
<div class="poster">
  <div class="sheet">
    <svg class="portrait-area" viewBox="0 0 708 775" role="img" aria-label="Large faint grey portrait silhouette of the leader behind the quotes">
      <defs>
        <radialGradient id="portraitTone" cx="50%" cy="45%" r="65%">
          <stop offset="0%" stop-color="#d2d2d2"/>
          <stop offset="100%" stop-color="#e2e2e2"/>
        </radialGradient>
      </defs>
      <path d="M250 0 H590 V640 Q660 720 708 775 H0 Q60 700 210 640 V40 Q210 0 250 0 Z" fill="url(#portraitTone)"/>
    </svg>

    <p class="quote-mark quote-mark--open" aria-hidden="true">&ldquo;</p>
    <p class="quote-mark quote-mark--close" aria-hidden="true">&rdquo;</p>

    <ul class="quotes">
      <li><span class="lead-letter">B</span>eing responsible sometimes means pissing people off.</li>
      <li>The day soldiers stop bringing you their problems is the day you have stopped leading them.</li>
      <li>Don't be buffaloed by experts and elites. Experts often possess more data than judgment.<br>Elites can become so inbred that they produce hemophiliacs who bleed to death as<br>soon as they are nicked by the real world.</li>
      <li>Don't be afraid to challenge the pros, even in their own backyard.</li>
      <li>Never neglect details. When everyone's mind is dulled or distracted the leader<br>must be doubly vigilant.</li>
      <li>You don't know what you can get away with until you try.</li>
      <li>Keep looking below surface appearances. Don't shrink from doing so (just) because<br>you might not like what you find.</li>
      <li>Organization doesn't really accomplish anything. Plans don't accomplish anything, either.<br>Theories of management don't much matter. Endeavors succeed or fail because of the<br>people involved. Only by attracting the best people will you accomplish great deeds.</li>
      <li>Organization charts and fancy titles count for next to nothing.</li>
      <li>Never let your ego get so close to your position that when your position goes,<br>your ego goes with it.</li>
      <li>Fit no stereotypes. Don't chase the latest management fads. The situation dictates<br>which approach best accomplishes the team's mission.</li>
      <li>Perpetual optimism is a force multiplier.</li>
      <li>Look for intelligence and judgment, and most critically, a capacity to anticipate, to see around<br>corners. Also look for loyalty, integrity, a high energy drive, a balanced ego, and the drive<br>to get things done.</li>
      <li>Great leaders are almost always great simplifiers, who can cut through argument, debate<br>and doubt, to offer a solution everybody can understand.</li>
      <li>The commander in the field is always right and the rear echelon is wrong, unless proved<br>otherwise.</li>
      <li>Have fun in your command. Don't always run at a breakneck pace. Take leave when you've<br>earned it: Spend time with your families. Corollary: surround yourself with people who<br>take their work seriously, but not themselves, those who work hard and play hard.</li>
      <li>Command is lonely.</li>
      <li>Leadership is the art of accomplishing more than the science of management says is possible.</li>
    </ul>
  </div>
</div>
</body>
</html>
```